Business Card for Lorena Whitfield

Name: Lorena Whitfield
Title: Realtor
Email: Lorena@LorenaWhitfieldRE.com
Phone: 480-555-0137

On the front of the business card, I would like the photo, the contact information and the Lorena Whitfield Logo. The backside is required to have the Broker logo and the required logos. Please use the colors from the logo design. Our company has a classy, professional look.

```html
<!DOCTYPE html>
<html lang="en">
<head>
<meta charset="UTF-8">
<title>Lorena Whitfield – Business Card</title>
<link href="https://fonts.googleapis.com/css2?family=Montserrat:ital,wght@0,400;0,500;1,500&display=swap" rel="stylesheet">
<style>
  :root {
    --brand-red: #c0112b;
    --ink-grey: #4a4a4a;
    --icon-grey: #555555;
    --paper: #f4f4f4;
    --backdrop: #e2e2e2;
    --badge: #1a1a1a;
    --photo-light: #9a9a9a;
    --photo-dark: #2e2e2e;
  }
  * { box-sizing: border-box; margin: 0; padding: 0; }
  html, body { width: 1200px; height: 900px; overflow: hidden; }
  body {
    background: var(--backdrop);
    font-family: "Montserrat", sans-serif;
    display: flex;
    flex-direction: column;
    align-items: center;
    justify-content: center;
    gap: 36px;
  }
  .card {
    position: relative;
    width: 660px;
    height: 377px;
    background: var(--paper);
    overflow: hidden;
    box-shadow: 0 2px 10px rgba(0,0,0,0.12);
  }

  /* Front */
  .brand-lockup {
    position: absolute;
    left: 28px;
    top: 36px;
    display: flex;
    align-items: center;
    gap: 14px;
  }
  .brand-mark {
    width: 58px;
    height: 58px;
    border: 3px solid var(--brand-red);
  }
  .brand-name {
    color: var(--brand-red);
    font-weight: 500;
    font-size: 22px;
    letter-spacing: 1px;
    line-height: 1.15;
    text-transform: uppercase;
  }
  .agent {
    position: absolute;
    left: 26px;
    top: 160px;
  }
  .agent-name {
    color: var(--brand-red);
    font-style: italic;
    font-weight: 500;
    font-size: 30px;
    line-height: 1.1;
  }
  .agent-title {
    color: var(--ink-grey);
    font-size: 18px;
    margin-top: 6px;
  }
  .contact-list {
    position: absolute;
    left: 26px;
    top: 280px;
    list-style: none;
  }
  .contact-item {
    display: flex;
    align-items: center;
    gap: 16px;
    color: var(--brand-red);
    font-size: 18px;
    font-weight: 500;
    height: 30px;
  }
  .contact-icon {
    width: 24px;
    height: 24px;
    flex: none;
  }
  .portrait {
    position: absolute;
    right: 0;
    top: 38px;
    bottom: 0;
    width: 248px;
    background: linear-gradient(180deg, var(--photo-light) 0%, #6f6f6f 55%, var(--photo-dark) 100%);
  }

  /* Back */
  .broker-lockup {
    position: absolute;
    left: 70px;
    top: 84px;
    display: flex;
    align-items: center;
    gap: 14px;
  }
  .broker-mark {
    width: 56px;
    height: 56px;
    border-radius: 50%;
    border: 3px solid var(--ink-grey);
  }
  .broker-name {
    color: var(--ink-grey);
    font-weight: 500;
    font-size: 20px;
    letter-spacing: 2px;
    line-height: 1.2;
    text-transform: uppercase;
  }
  .accent-bar {
    position: absolute;
    height: 10px;
    background: var(--brand-red);
  }
  .accent-bar--upper { left: 70px; top: 180px; width: 180px; }
  .accent-bar--lower { left: 70px; top: 300px; width: 260px; }
  .compliance-badges {
    position: absolute;
    left: 360px;
    top: 246px;
    display: flex;
    gap: 14px;
    align-items: flex-end;
  }
  .badge {
    border: 3px solid var(--badge);
  }
  .badge--housing { width: 64px; height: 56px; }
  .badge--association { width: 56px; height: 56px; }
  .badge--listing { width: 84px; height: 44px; }
</style>
</head>
<body>

  <section class="card card--front" aria-label="Business card front">
    <div class="brand-lockup">
      <span class="brand-mark" aria-hidden="true"></span>
      <span class="brand-name">Lorena Whitfield<br>Real Estate</span>
    </div>

    <div class="agent">
      <h1 class="agent-name">Lorena Whitfield</h1>
      <p class="agent-title">Realtor</p>
    </div>

    <ul class="contact-list">
      <li class="contact-item">
        <svg class="contact-icon" viewBox="0 0 24 24" fill="none" stroke="var(--icon-grey)" stroke-width="1.5" stroke-linejoin="round" aria-hidden="true">
          <path d="M6 3l3 0 1.5 4.5-2 1.5a11 11 0 0 0 6.5 6.5l1.5-2 4.5 1.5v3a2 2 0 0 1-2 2A17 17 0 0 1 4 5a2 2 0 0 1 2-2z"/>
        </svg>
        <span>480-555-0137</span>
      </li>
      <li class="contact-item">
        <svg class="contact-icon" viewBox="0 0 24 24" fill="none" stroke="var(--icon-grey)" stroke-width="1.5" stroke-linejoin="round" aria-hidden="true">
          <rect x="2.5" y="5" width="19" height="14" rx="3"/>
          <path d="M3 7l9 6 9-6"/>
        </svg>
        <span>Lorena@LorenaWhitfieldRE.com</span>
      </li>
    </ul>

    <div class="portrait" role="img" aria-label="Black and white portrait photo of Lorena Whitfield"></div>
  </section>

  <section class="card card--back" aria-label="Business card back">
    <div class="broker-lockup">
      <span class="broker-mark" aria-hidden="true"></span>
      <span class="broker-name">Harlow Crest<br>Real Estate</span>
    </div>
    <div class="accent-bar accent-bar--upper"></div>

    <div class="compliance-badges" aria-label="Required compliance badges">
      <span class="badge badge--housing"></span>
      <span class="badge badge--association"></span>
      <span class="badge badge--listing"></span>
    </div>
    <div class="accent-bar accent-bar--lower"></div>
  </section>

</body>
</html>
```